Seaside commercial building needs a design for a prominent sign

we have bought a small commercial building in a small seaside area. The building was in disrepair and we are rebuilding it and will rent to small businesses. We have a tall sign right on the corner of the area and want to design something special for the sign The address is 2738 and we want to incorporate that into the name, or just have that as the name. The area is called Bonnet Shores which we were going to use and call it Tidewater Corner. Almost all shops, however use Bonnet in their name. Looking for something unique with a sea-related logo. Elegant, yet welcoming.

```html
<!DOCTYPE html>
<html lang="en">
<head>
<meta charset="utf-8">
<title>Tidewater Corner – Corner Sign</title>
<link rel="stylesheet" href="https://fonts.googleapis.com/css2?family=Grenze:wght@700&display=swap">
<style>
  :root {
    --page: #ffffff;
    --panel: #dfdfd9;
    --ink: #111111;
    --sea: #139aaf;
    --oval: #ffffff;
  }
  * { margin: 0; padding: 0; box-sizing: border-box; }
  html, body {
    width: 1200px;
    height: 1200px;
    overflow: hidden;
    background: var(--page);
  }
  .sign {
    position: relative;
    width: 1200px;
    height: 1200px;
    font-family: "Grenze", Georgia, serif;
    font-weight: 700;
    color: var(--ink);
  }
  .sign__head {
    position: absolute;
    left: 0;
    top: 0;
  }
  .sign__number {
    font-family: "Grenze", Georgia, serif;
    font-weight: 700;
    font-size: 84px;
    fill: var(--ink);
    letter-spacing: 1px;
  }
  .sign__name {
    position: absolute;
    left: 250px;
    top: 430px;
    width: 696px;
    height: 110px;
    display: flex;
    align-items: center;
    justify-content: center;
    gap: 18px;
    font-size: 70px;
    line-height: 1;
    font-variant: small-caps;
    letter-spacing: 1px;
  }
  .sign__dot {
    width: 34px;
    height: 34px;
    border-radius: 50%;
    background: var(--sea);
    flex: none;
  }
  .sign__band {
    position: absolute;
    left: 250px;
    width: 696px;
    height: 132px;
    background: var(--panel);
    display: flex;
    align-items: center;
    justify-content: center;
    font-size: 58px;
    font-variant: small-caps;
    letter-spacing: 2px;
    line-height: 1;
  }
  .sign__band--owner { top: 645px; }
  .sign__band--lease { top: 830px; }
</style>
</head>
<body>
  <main class="sign">
    <svg class="sign__head" width="1200" height="600" viewBox="0 0 1200 600" aria-hidden="true">
      <path d="M250 262 C350 262 420 250 480 222 C540 196 570 194 598 194 C626 194 656 196 716 222 C776 250 846 262 946 262 L946 582 L250 582 Z" fill="var(--panel)"/>
      <ellipse cx="598" cy="278" rx="111" ry="64" fill="var(--oval)"/>
      <text class="sign__number" x="598" y="310" text-anchor="middle">2738</text>
    </svg>

    <div class="sign__name">
      <span class="sign__dot"></span>
      <span>Tidewater Corner</span>
    </div>

    <div class="sign__band sign__band--owner">Harlow Properties</div>
    <div class="sign__band sign__band--lease">For Lease</div>
  </main>
</body>
</html>
```